Amber Ridge Publishing Web Page Design

Design a website for my new start up publishing company - Amber Ridge Publishing, the first work published by ARP with be a new book by T.R. Menshaw called Silent Harbor. The prototype for the book cover is attached.

Target Market(s)

Worldwide, all readers of mystery, fiction, etc.

Industry/Entity Type

Book Publisher

Coding

Coded - Design and coding required

Number of Pages Required

1 page

```html
<!DOCTYPE html>
<html lang="en">
<head>
<meta charset="utf-8">
<title>Amber Ridge Publishing</title>
<link href="https://fonts.googleapis.com/css2?family=Lato:ital,wght@0,400;0,700;0,900;1,400&family=Ubuntu:wght@500;700&display=swap" rel="stylesheet">
<style>
:root{
  --green:#94c83d;
  --green-dark:#7cb32a;
  --ink:#151b24;
  --ink-soft:#1d2530;
  --text:#333;
  --white:#fff;
  --star:#e0b13a;
  --cover-yellow:#f2d21b;
  --cover-cyan:#38c6e0;
}
*{box-sizing:border-box;margin:0;padding:0}
html,body{width:1200px;height:4501px;overflow:hidden}
body{position:relative;font-family:"Lato",sans-serif;color:var(--text);background:var(--white)}
.abs{position:absolute}
h1,h2,h3{font-family:"Ubuntu",sans-serif;font-weight:500}

/* header */
.topbar{top:0;left:0;width:1200px;height:77px;background:var(--white)}
.brand{left:128px;top:20px;display:flex;align-items:center;gap:12px;font-size:22px;color:#444}
.brand .mark{width:30px;height:30px;border-radius:50%;background:var(--green)}
.contact{top:20px;display:flex;align-items:center;gap:14px;font-size:16px;color:#333}
.contact.mail{left:606px}
.contact.phone{left:880px;font-weight:700;font-size:19px}
.nav{top:77px;left:0;width:1200px;height:54px;background:var(--green);display:flex;justify-content:center;gap:48px;align-items:center}
.nav a{color:var(--white);text-decoration:none;font-size:18px;position:relative}
.nav a.active::after{content:"";position:absolute;left:-6px;right:-6px;bottom:-9px;height:2px;background:var(--white)}

/* hero */
.hero{top:131px;left:0;width:1200px;height:611px;background:linear-gradient(120deg,#3c3a36 0%,#7a6c5a 40%,#b6a78e 70%,#5a5246 100%)}
.hero-title{top:298px;left:0;width:1200px;text-align:center;color:var(--white);font-family:"Ubuntu",sans-serif;font-weight:700;font-size:76px;line-height:92px;text-shadow:0 3px 6px rgba(0,0,0,.55)}
.circle-btn{width:56px;height:56px;border-radius:50%;background:var(--white);display:flex;align-items:center;justify-content:center}
.dots{display:flex;gap:10px;justify-content:center}
.dots i{width:16px;height:16px;border-radius:50%;background:var(--white);border:2px solid var(--white)}
.dots i.off{background:transparent}
.hero-wave{top:640px;left:0}

/* about */
.about-title{top:845px;left:118px;font-size:58px;color:#111}
.about-text{top:948px;left:110px;width:645px;font-size:14.5px;line-height:31.8px;text-align:justify;color:#333}
.btn-dark{top:1213px;left:111px;width:152px;height:60px;background:var(--ink);color:var(--white);font-size:18px;font-weight:700;display:flex;align-items:center;justify-content:center}
.book{top:826px;left:816px;width:272px;height:432px;transform:skewY(4deg);box-shadow:6px 8px 14px rgba(0,0,0,.35)}
.book-art{position:absolute;inset:0;background:linear-gradient(160deg,#2a3350 0%,#1a2340 45%,#3d4f8a 75%,#1b2236 100%);border-right:8px solid #e9e9ee}
.book-title{position:absolute;top:50px;left:20px;right:20px;text-align:center;font-family:"Ubuntu",sans-serif;font-weight:700;font-size:46px;line-height:48px;color:var(--cover-yellow);text-transform:uppercase}
.book-author{position:absolute;bottom:36px;left:20px;right:20px;text-align:center;font-family:"Ubuntu",sans-serif;font-weight:700;font-size:28px;color:var(--cover-cyan);letter-spacing:1px}

/* featured */
.featured{top:1377px;left:0;width:1200px;height:733px;background:radial-gradient(ellipse at 70% 40%,#2a3440 0%,var(--ink-soft) 45%,var(--ink) 100%)}
.featured-title{top:1478px;left:0;width:1200px;text-align:center;color:var(--white);font-size:58px}
.featured-text{top:1617px;left:255px;width:690px;text-align:center;color:#e8e8e8;font-size:14.5px;line-height:35px}
.cover{top:1782px;height:239px;border:4px solid var(--white)}
.cover-art{position:absolute;inset:0}
.cover.gold .cover-art{background:linear-gradient(160deg,#000 0%,#000 55%,#6b5318 75%,#c8a23a 90%,#111 100%)}
.cover.snow .cover-art{background:linear-gradient(180deg,#e6e6e6 0%,#cfcfcf 55%,#f2f2f2 70%,#9a9a9a 100%)}
.cover-label{position:absolute;top:18px;left:0;right:0;text-align:center;font-size:17px;color:var(--white)}
.cover.snow .cover-label{top:12px;font-weight:700;font-size:15px;color:#333;line-height:15px}
.cover.snow .cover-label small{display:block;font-weight:400;font-size:12px;color:#aaa}

/* services */
.services-title{top:2195px;left:0;width:1200px;text-align:center;font-size:58px;color:#111}
.service{top:2326px;width:300px;text-align:center}
.service .icon{width:88px;height:88px;margin:0 auto;border-radius:50%;background:var(--green);border:5px solid var(--ink);border-bottom-color:var(--green);border-left-color:var(--green);display:flex;align-items:center;justify-content:center}
.service h3{margin-top:28px;font-size:30px;color:#222}
.service p{margin-top:22px;font-size:14.5px;line-height:32px;text-align:justify;text-align-last:center;color:#333}
.dark-dots{top:2656px;left:0;width:1200px;display:flex;gap:10px;justify-content:center}
.dark-dots i{width:13px;height:13px;border-radius:50%;background:var(--ink)}

/* authors */
.authors{top:2743px;left:0;width:1200px;height:669px;background:radial-gradient(ellipse at 50% 40%,#b2d95a 0%,var(--green) 55%,var(--green-dark) 100%)}
.authors-title{top:2822px;left:0;width:1200px;text-align:center;color:var(--white);font-size:58px;font-weight:700}
.portrait{top:2987px;width:252px;height:275px;border:2px solid var(--white)}
.portrait.p1{left:171px;background:linear-gradient(160deg,#5b4632,#8a7a6a 50%,#cfd3d8)}
.portrait.p2{left:463px;background:linear-gradient(160deg,#3a2c22,#6d5440 55%,#9c8a78)}
.portrait.p3{left:763px;background:linear-gradient(160deg,#f1e3b0,#d7c23e 55%,#6d7a2c)}
.author-name{top:3295px;width:300px;text-align:center;color:var(--white);font-family:"Ubuntu",sans-serif;font-weight:700;font-size:21px}

/* testimonials */
.testi-title{top:3505px;left:0;width:1200px;text-align:center;font-size:58px;font-weight:700;color:#111}
.avatar{top:3600px;left:554px;width:92px;height:92px;border-radius:50%;background:linear-gradient(160deg,#e46a2e,#a9331c);border:3px solid #f4c9b6}
.testi-text{top:3710px;left:330px;width:540px;text-align:center;font-size:14.5px;line-height:30px}
.testi-org{top:3813px;left:0;width:1200px;text-align:center;font-style:italic;font-size:14px;color:#555}
.testi-name{top:3838px;left:0;width:1200px;text-align:center;font-style:italic;font-size:14px;color:#555}
.stars{top:3870px;left:0;width:1200px;display:flex;justify-content:center}
.testi-dots{top:3924px;left:0;width:1200px;display:flex;gap:8px;justify-content:center}
.testi-dots i{width:15px;height:15px;border-radius:50%;background:var(--ink);border:2px solid var(--ink)}
.testi-dots i.off{background:transparent}

/* footer */
.footer-wave{top:3960px;left:0}
.footer{top:4040px;left:0;width:1200px;height:394px;background:var(--ink)}
.foot-title{top:4128px;color:var(--white);font-size:16px;font-weight:700;letter-spacing:.3px}
.foot-title::after{content:"";display:block;width:60px;height:3px;background:var(--green);margin-top:24px}
.quick{top:4207px;left:125px;list-style:none;color:var(--white);font-size:12.5px;line-height:31px}
.quick li:nth-child(5){padding-left:3px}
.info{left:388px;color:var(--white);font-size:12.5px;line-height:22px;display:flex;gap:14px}
.news{top:4208px;left:730px;width:336px;height:44px;border-radius:22px;background:var(--white);display:flex;align-items:center;justify-content:space-between;padding-left:22px;font-size:12px;color:#888;border:2px solid var(--white)}
.news .send{height:40px;width:96px;border-radius:20px;background:var(--ink);color:var(--white);font-weight:700;font-size:13px;display:flex;align-items:center;justify-content:center}
.social{top:4297px;left:736px;display:flex;gap:31px}
.social i{width:18px;height:18px;border-radius:50%;background:var(--white)}
.bottom{top:4434px;left:0;width:1200px;height:67px;background:#0b0f15;color:var(--white);font-size:12.5px;display:flex;align-items:center;padding-left:113px}
</style>
</head>
<body>

<header>
  <div class="abs topbar"></div>
  <div class="abs brand"><span class="mark"></span><span>Amber Ridge</span></div>
  <div class="abs contact mail">
    <svg width="40" height="30" viewBox="0 0 40 30"><rect x="1" y="2" width="38" height="26" rx="2" fill="var(--green)"/><path d="M2 4l18 13L38 4" stroke="#fff" stroke-width="2.5" fill="none"/></svg>
    <span>info@amberridge.example</span>
  </div>
  <div class="abs contact phone">
    <svg width="40" height="40" viewBox="0 0 40 40"><circle cx="20" cy="20" r="18" fill="none" stroke="var(--green)" stroke-width="2.5"/><path d="M13 11c2-1 3 0 4 3s-1 3 0 5 3 4 5 5 2-2 5 0 2 3 0 5-8 0-12-5-4-12-2-13z" fill="var(--green)"/></svg>
    <span>+ 555 010 2040</span>
  </div>
  <nav class="abs nav">
    <a class="active" href="#">Home</a><a href="#">About Us</a><a href="#">Author</a><a href="#">Our Publishing</a><a href="#">Blog</a><a href="#">Contact Us</a>
  </nav>
</header>

<section class="hero-block">
  <div class="abs hero" role="img" aria-label="Photo of a writer at a desk with a laptop, glasses and notebook"></div>
  <h1 class="abs hero-title">Welcome To<br>Amber Ridge</h1>
  <div class="abs circle-btn" style="left:115px;top:363px"><svg width="20" height="20" viewBox="0 0 20 20"><path d="M17 10H4M9 4l-6 6 6 6" stroke="#222" stroke-width="2.4" fill="none"/></svg></div>
  <div class="abs circle-btn" style="left:1033px;top:363px"><svg width="20" height="20" viewBox="0 0 20 20"><path d="M3 10h13M11 4l6 6-6 6" stroke="#222" stroke-width="2.4" fill="none"/></svg></div>
  <div class="abs dots" style="top:635px;left:0;width:1200px"><i></i><i></i><i class="off"></i></div>
  <svg class="abs hero-wave" width="1200" height="110" viewBox="0 0 1200 110">
    <path d="M0 40 C200 100 400 100 700 60 C900 35 1080 30 1200 30 L1200 110 L0 110Z" fill="#fff"/>
    <path d="M0 40 C200 110 420 110 700 62 C900 32 1080 28 1200 30 L1200 36 C1080 36 900 46 700 76 C420 118 180 108 0 55Z" fill="var(--green)"/>
  </svg>
</section>

<section class="about">
  <h2 class="abs about-title">About us</h2>
  <p class="abs about-text">Lorem ipsum dolor sit amet, consectetur adipiscing elit, sed do eiusmod tempor incididunt ut labore et dolore magna aliqua. Quis ipsum suspendisse ultrices gravida. Risus commodo viverra maecenas accumsan lacus vel facilisis. Lorem ipsum dolor sit amet, consectetur adipiscing elit, sed do eiusmod tempor incididunt ut labore et dolore magna aliqua. Quis ipsum suspendisse ultrices gravida. Risus commodo viverra maecenas accumsan lacus vel facilisis. Lorem ipsum dolor sit amet, consectetur adipiscing elit, sed do eiusmod tempor incididunt ut labore et dolore magna aliqua. Quis ipsum suspendisse ultrices gravida.</p>
  <div class="abs btn-dark">Read More</div>
  <div class="abs book">
    <div class="book-art" role="img" aria-label="Cover art for Silent Harbor: a dark blue stormy night with lightning"></div>
    <div class="book-title">Silent<br>Harbor</div>
    <div class="book-author">T.R. MENSHAW</div>
  </div>
</section>

<section class="featured-block">
  <div class="abs featured" role="img" aria-label="Dark background with an open book"></div>
  <h2 class="abs featured-title">Featured Product</h2>
  <p class="abs featured-text">Lorem ipsum dolor sit amet, consectetur adipiscing elit, sed do eiusmod tempor incididunt ut labore et dolore magna aliqua. Quis ipsum suspendisse ultrices gravida. Risus commodo viverra maecenas ac-cumsan lacus vel facilisis. Risus commodo viverra maecenas accumsan lacus vel facilisis. Risus commodo viverra maecenas accumsan lacus vel facilisis.</p>
  <div class="abs cover gold" style="left:290px;width:187px">
    <div class="cover-art" role="img" aria-label="Black book cover with gold brush strokes"></div>
    <div class="cover-label">Lorem ipsum dolor</div>
  </div>
  <div class="abs cover snow" style="left:508px;width:184px">
    <div class="cover-art" role="img" aria-label="Book cover with a lone bare tree in a snowy field"></div>
    <div class="cover-label">LOREM IPSUM<small>AUTHOR NAME</small></div>
  </div>
  <div class="abs cover gold" style="left:730px;width:187px">
    <div class="cover-art" role="img" aria-label="Black book cover with gold brush strokes"></div>
    <div class="cover-label">Lorem ipsum dolor</div>
  </div>
</section>

<section class="services">
  <h2 class="abs services-title">Services</h2>
  <div class="abs service" style="left:109px">
    <div class="icon"><svg width="38" height="38" viewBox="0 0 38 38" fill="none" stroke="#fff" stroke-width="2"><rect x="7" y="5" width="20" height="27" rx="2"/><path d="M11 12h12M11 17h12M11 22h7M22 30l10-12 3 3-10 12h-3z"/></svg></div>
    <h3>Editing</h3>
    <p>Lorem ipsum dolor sit amet, consectetur adipiscing elit, sed do eiusmod tempor incididunt ut labore et dolore.</p>
  </div>
  <div class="abs service" style="left:457px">
    <div class="icon"><svg width="38" height="38" viewBox="0 0 38 38" fill="none" stroke="#fff" stroke-width="2"><rect x="6" y="6" width="26" height="26" rx="2"/><path d="M10 12h18M10 17h8M10 22h8M10 27h8M22 17h6v10h-6z"/></svg></div>
    <h3>Marketing</h3>
    <p>Lorem ipsum dolor sit amet, consectetur adipiscing elit, sed do eiusmod tempor incididunt ut labore et dolore.</p>
  </div>
  <div class="abs service" style="left:795px">
    <div class="icon"><svg width="38" height="38" viewBox="0 0 38 38" fill="none" stroke="#fff" stroke-width="2"><rect x="10" y="14" width="18" height="18" rx="2"/><path d="M10 20h18M10 26h18M13 9h12M19 5v9"/><circle cx="10" cy="8" r="2"/><circle cx="28" cy="8" r="2"/></svg></div>
    <h3>Distribution</h3>
    <p>Lorem ipsum dolor sit amet, consectetur adipiscing elit, sed do eiusmod tempor incididunt ut labore et dolore.</p>
  </div>
  <div class="abs dark-dots"><i></i><i></i><i></i></div>
</section>

<section class="authors-block">
  <div class="abs authors"></div>
  <h2 class="abs authors-title">Our&nbsp; Author</h2>
  <svg class="abs" style="left:95px;top:3110px" width="40" height="30" viewBox="0 0 40 30"><path d="M36 15H6M18 3L5 15l13 12" stroke="#fff" stroke-width="4" fill="none"/></svg>
  <svg class="abs" style="left:1070px;top:3110px" width="40" height="30" viewBox="0 0 40 30"><path d="M4 15h30M22 3l13 12-13 12" stroke="#fff" stroke-width="4" fill="none"/></svg>
  <div class="abs portrait p1" role="img" aria-label="Portrait of a senior author in front of bookshelves"></div>
  <div class="abs portrait p2" role="img" aria-label="Author typing at a vintage typewriter"></div>
  <div class="abs portrait p3" role="img" aria-label="Author writing in a notebook in warm sunlight"></div>
  <div class="abs author-name" style="left:147px">Lorem ipsum doloring</div>
  <div class="abs author-name" style="left:439px">Lorem ipsum doloring</div>
  <div class="abs author-name" style="left:739px">Lorem ipsum doloring</div>
</section>

<section class="testi">
  <h2 class="abs testi-title">Testimonials</h2>
  <div class="abs avatar" role="img" aria-label="Reviewer portrait"></div>
  <p class="abs testi-text">Lorem ipsum dolor sit amet, consectetur adipiscing elit, sed do eiusmod tempor incididunt ut labore et dolore magna aliqua. Quis ipsum suspendisse ultrices gravida. Risus commodo viverra maecenas accumsan lacus vel facilisis.</p>
  <div class="abs testi-org">Reading Forward Trust</div>
  <div class="abs testi-name">Mara Ellison</div>
  <div class="abs stars">
    <svg width="110" height="22" viewBox="0 0 110 22">
      <defs><path id="st" d="M10 1l2.8 6 6.4.6-4.8 4.3 1.4 6.4L10 15l-5.8 3.3 1.4-6.4L.8 7.6l6.4-.6z"/></defs>
      <use href="#st" x="0" fill="var(--star)"/><use href="#st" x="22" fill="var(--star)"/><use href="#st" x="44" fill="var(--star)"/><use href="#st" x="66" fill="var(--star)"/><use href="#st" x="88" fill="#aaa"/>
    </svg>
  </div>
  <div class="abs testi-dots"><i></i><i></i><i class="off"></i></div>
</section>

<footer>
  <svg class="abs footer-wave" width="1200" height="84" viewBox="0 0 1200 84">
    <path d="M0 70 C300 30 600 20 850 25 C1000 28 1120 45 1200 70 L1200 84 L0 84Z" fill="var(--ink)"/>
    <path d="M0 70 C300 22 600 6 850 12 C1000 16 1120 40 1200 70 C1120 50 1000 34 850 30 C600 24 300 36 0 74Z" fill="var(--green)"/>
  </svg>
  <div class="abs footer"></div>
  <div class="abs foot-title" style="left:122px">QUICKLINKS</div>
  <div class="abs foot-title" style="left:388px">CONTACT US</div>
  <div class="abs foot-title" style="left:735px">NEWSLETTER</div>
  <ul class="abs quick"><li>Home</li><li>About Us</li><li>Author</li><li>Our Publishing</li><li>Blog</li><li>Contact Us</li></ul>
  <div class="abs info" style="top:4214px">
    <svg width="18" height="22" viewBox="0 0 18 22"><path d="M9 1a7 7 0 017 7c0 5-7 13-7 13S2 13 2 8a7 7 0 017-7z" fill="#fff"/><circle cx="9" cy="8" r="2.6" fill="var(--ink)"/></svg>
    <span>Level 12, 40 Harbour Lane<br>Portside 2000</span>
  </div>
  <div class="abs info" style="top:4276px">
    <svg width="18" height="18" viewBox="0 0 18 18"><path d="M3 2c2-1 3 0 4 3s-1 2 0 4 3 3 4 4 2-1 4 0 1 3 0 4-7 0-10-4S1 3 3 2z" fill="#fff"/></svg>
    <span>Tel: +555 010 2040</span>
  </div>
  <div class="abs info" style="top:4318px">
    <svg width="18" height="14" viewBox="0 0 18 14"><rect width="18" height="14" rx="1" fill="#fff"/><path d="M1 1l8 6 8-6" stroke="var(--ink)" stroke-width="1.5" fill="none"/></svg>
    <span>Email: info@amberridge.example</span>
  </div>
  <div class="abs news"><span>Enter Email Address</span><span class="send">SEND</span></div>
  <div class="abs social"><i></i><i></i><i></i><i></i><i></i></div>
  <div class="abs bottom">© 2019 Copyrights Amber Ridge Publishing | All Rights Reserved</div>
</footer>

</body>
</html>
```